Consultancy Report Template in Word (Preferably in Google Docs)

I require a professional Google Doc Template that I will use for Professional Consultancy reports.
Using the brand guidelines attached as a base, I'd like the report themed in the brand colours.
It must look professional but I'd like some creative licence to be shown.
Feel free to pull some sample images from the website - www.vantrelo.com.au that I can replace with site specific images on the cover and within the template.
As a minimum, it must have:
Very presentable cover page
Table of contents (set up linked to headers)
Section Headings - (SECTION NAME) potentially Full Page 'semi-cover pages' or presentable banners
Sub Section Headings ( 1 - TOPIC XXX)
Sub Clauses (1.1 - TOPIC XXX)
Presentable Tables in brand colours that can be expanded to more or fewer columns and rows.
Rear Cover Page
Headers and footers

```html
<!DOCTYPE html>
<html lang="en">
<head>
<meta charset="utf-8">
<title>Commercial Wastewater – Report Template</title>
<link rel="stylesheet" href="https://fonts.googleapis.com/css2?family=Montserrat:wght@400;500;600;700&display=swap">
<style>
:root{
  --backdrop:#d5cbca;
  --paper:#ffffff;
  --brand-blue:#2f9fe0;
  --deep-blue:#1d6fb2;
  --accent-pink:#c77fd3;
  --lilac:#b89bd6;
  --lilac-soft:#efe6f4;
  --lilac-mid:#ddcdea;
  --ink:#333a44;
  --muted:#6b7280;
  --rule:#c8d6e6;
}
*{margin:0;padding:0;box-sizing:border-box}
html,body{width:1200px;height:2224px;overflow:hidden}
body{background:var(--backdrop);font-family:"Montserrat",sans-serif;color:var(--ink);position:relative}
.page{position:absolute;width:530px;height:650px;background:var(--paper);overflow:hidden;box-shadow:0 2px 6px rgba(0,0,0,.08)}
.p-cover{left:82px;top:77px}
.p-contents{left:652px;top:77px}
.p-three{left:82px;top:786px}
.p-four{left:652px;top:786px}
.p-five{left:82px;top:1491px}
.p-six{left:652px;top:1491px}

/* running header & footer */
.running-head{position:absolute;left:28px;right:28px;top:14px;height:18px;border-bottom:1px solid var(--rule);display:flex;justify-content:space-between;align-items:center;font-size:8px;z-index:2}
.running-head .doc-title{color:var(--lilac);font-weight:600;letter-spacing:.3px}
.running-head .site{color:var(--brand-blue);font-size:6.5px}
.folio{position:absolute;right:24px;bottom:14px;width:22px;height:14px;background:var(--lilac-mid);color:var(--deep-blue);font-size:6.5px;font-weight:600;display:flex;align-items:center;justify-content:center}

.body-text{font-size:7.4px;line-height:1.45;color:var(--ink)}
.h-section{font-size:24px;font-weight:700;color:var(--ink)}
.h-sub{font-size:19px;font-weight:600;color:var(--ink)}
.photo{position:absolute;background:linear-gradient(160deg,#8db9d9 0%,#7f9a6e 55%,#5f7b4a 100%)}

/* cover */
.cover-title{position:absolute;left:0;right:0;top:48px;text-align:center;font-size:24px;font-weight:700;color:var(--deep-blue);letter-spacing:.6px}
.cover-tag{position:absolute;left:0;right:0;top:86px;display:flex;justify-content:center;align-items:center;gap:8px;font-size:7.5px;letter-spacing:1px;color:var(--accent-pink);font-weight:500}
.cover-tag::before,.cover-tag::after{content:"";width:58px;height:1px;background:var(--lilac)}
.cover-band{position:absolute;left:0;right:0;top:297px;bottom:0;background:var(--brand-blue)}
.cover-rings{position:absolute;left:131px;top:141px}
.cover-photo{left:170px;top:180px;width:232px;height:232px;border-radius:50%;background:linear-gradient(180deg,#9cc8ea 0%,#5a9fcf 30%,#c9b48c 55%,#7d8f5c 100%)}
.brand-lockup{position:absolute;left:0;right:0;top:520px;display:flex;justify-content:center;align-items:center;gap:12px;color:#fff;font-size:17px;font-weight:500;letter-spacing:1.5px;line-height:1.15}
.brand-lockup .mark{width:46px;height:46px;border:2px solid #fff;border-radius:50%}
.cover-fields{position:absolute;left:34px;right:34px;top:610px;display:flex;gap:30px;color:#fff;font-size:7.5px}
.cover-fields span{flex:1;border-bottom:1px solid rgba(255,255,255,.8);padding-bottom:3px}

/* contents */
.contents-stripe{position:absolute;left:0;top:0;bottom:0;width:143px;background:var(--brand-blue)}
.contents-brand{position:absolute;right:30px;top:44px;display:flex;align-items:center;gap:6px;font-size:8px;font-weight:500;color:var(--deep-blue);letter-spacing:.8px;line-height:1.2}
.contents-brand .mark{width:18px;height:18px;border:1.5px solid var(--deep-blue);border-radius:50%}
.contents-title{position:absolute;left:174px;top:150px;font-size:16px;font-weight:700;color:var(--deep-blue);letter-spacing:.4px}
.toc{position:absolute;left:174px;width:320px;display:flex;align-items:flex-end;font-size:8px;color:var(--ink)}
.toc .dots{flex:1;border-bottom:1px solid #9aa4b0;margin:0 4px 2px}
.toc.level-1{font-size:10.5px;font-weight:500}
.toc .num{color:var(--ink)}

/* page three */
.intro-band{position:absolute;left:0;right:0;top:40px;height:262px;background:var(--lilac-soft)}
.portrait{left:30px;top:58px;width:162px;height:162px;border-radius:50%;border:4px solid var(--lilac);background:linear-gradient(180deg,#a9cbe6 0%,#a9cbe6 45%,#6e8e58 46%,#55723f 100%)}
.intro-heading{position:absolute;left:266px;top:84px}
.intro-text{position:absolute;left:266px;top:120px;width:236px}
.icon-row{position:absolute;left:30px;right:30px;display:flex;align-items:center;gap:18px}
.icon-row.flip{flex-direction:row-reverse}
.icon-badge{flex:none;width:50px;height:50px;border-radius:50%;background:var(--lilac-soft);border:1.5px solid var(--lilac);display:flex;align-items:center;justify-content:center}
.icon-row .body-text{flex:1}

/* page four */
.two-col{position:absolute;left:30px;right:30px;display:flex;gap:22px}
.two-col > *{flex:1}
.bullet-head{font-size:7.5px;font-weight:700;display:flex;gap:5px;align-items:center;margin-bottom:2px}
.bullet-head::before{content:"";width:5px;height:5px;background:var(--brand-blue);border-radius:50%}
.bullet-body{font-size:9px;line-height:1.4;padding-left:10px}

/* page five table */
.table-band{position:absolute;left:0;right:0;top:40px;height:250px;background:var(--lilac-soft)}
.data-table{position:absolute;left:33px;top:128px;width:465px;border-collapse:collapse;font-size:6.5px}
.data-table th{background:var(--brand-blue);color:#fff;font-weight:600;height:15px;border:1px solid #fff}
.data-table td{height:16px;border:1px solid #fff;text-align:center;background:#fff;font-size:10px;color:var(--ink)}
.data-table td.row-label{background:var(--lilac-mid);font-size:6.5px;text-align:left;padding-left:8px;color:var(--ink)}
.data-table tr:nth-child(even) td{background:#f6f1f9}
.data-table tr:nth-child(even) td.row-label{background:#cdb8e0}
</style>
</head>
<body>

<!-- Cover -->
<section class="page p-cover">
  <div class="cover-title">COMMERCIAL WASTEWATER</div>
  <div class="cover-tag">SIMPLIFYING COMMERCIAL WASTEWATER</div>
  <div class="cover-band"></div>
  <svg class="cover-rings" width="310" height="310" viewBox="0 0 310 310" aria-hidden="true">
    <path d="M250 52 A140 140 0 1 0 292 185" fill="none" stroke="#b89bd6" stroke-width="7"/>
    <path d="M228 46 A128 128 0 0 0 40 120" fill="none" stroke="#efe6f4" stroke-width="3"/>
  </svg>
  <div class="photo cover-photo" role="img" aria-label="Coastal commercial site with cabins by the sea"></div>
  <div class="brand-lockup"><span class="mark"></span><span>VANTRELO<br>WASTEWATER</span></div>
  <div class="cover-fields"><span>Client Name:</span><span>Date:</span></div>
</section>

<!-- Table of contents -->
<section class="page p-contents">
  <div class="contents-stripe"></div>
  <div class="contents-brand"><span class="mark"></span><span>VANTRELO<br>WASTEWATER</span></div>
  <div class="contents-title">TABLE OF CONTENTS</div>
  <div class="toc level-1" style="top:186px">Heading 1<span class="dots"></span><span class="num">02</span></div>
  <div class="toc" style="top:212px">Heading 2.1<span class="dots"></span><span class="num">03</span></div>
  <div class="toc" style="top:232px">Heading 2.2<span class="dots"></span><span class="num">04</span></div>
  <div class="toc level-1" style="top:258px">Heading 2<span class="dots"></span><span class="num">05</span></div>
  <div class="toc" style="top:282px">Heading 2.1<span class="dots"></span><span class="num">06</span></div>
  <div class="toc" style="top:301px">Heading 2.2<span class="dots"></span><span class="num">07</span></div>
  <div class="toc level-1" style="top:324px">Heading 3<span class="dots"></span><span class="num">08</span></div>
  <div class="toc" style="top:348px">Heading 3.1<span class="dots"></span><span class="num">09</span></div>
  <div class="toc" style="top:368px">Heading 3.2<span class="dots"></span><span class="num">10</span></div>
  <div class="toc level-1" style="top:397px">Heading 4<span class="dots"></span><span class="num">11</span></div>
  <div class="toc" style="top:420px">Heading 4.1<span class="dots"></span><span class="num">12</span></div>
  <div class="toc" style="top:440px">Heading 4.2<span class="dots"></span><span class="num">13</span></div>
</section>

<!-- Section 1 -->
<section class="page p-three">
  <header class="running-head"><span class="doc-title">COMMERCIAL WASTEWATER</span><span class="site">www.vantrelo.com.au</span></header>
  <div class="intro-band"></div>
  <div class="photo portrait" role="img" aria-label="Consultant standing beside a treatment system on a lawn"></div>
  <h1 class="h-section intro-heading">1. Heading Here</h1>
  <p class="body-text intro-text">Lorem ipsum dolor sit amet, consectetur adipiscing elit, sed do eiusmod tempor incididunt ut labore et dolore magna aliqua. Quis ipsum suspendisse ultrices gravida. Risus commodo viverra maecenas accumsan lacus vel facilisis. Lorem Ipsum is simply dummy text of the printing and typesetting industry. Lorem Ipsum has been the industry's standard dummy text ever since the 1500s, when an unknown printer took a galley of type and scrambled it to make a type specimen book. It has survived not only five centuries, but also the leap into electronic typesetting, remaining essentially unchanged. It was popularised.</p>
  <h2 class="h-sub" style="position:absolute;left:30px;top:330px">1.1 Heading Here</h2>
  <div class="icon-row" style="top:372px">
    <span class="icon-badge"><svg width="22" height="22" viewBox="0 0 22 22"><path d="M3 19V9l8-6 8 6v10H3z M9 19v-6h4v6" fill="none" stroke="#2f9fe0" stroke-width="1.5"/></svg></span>
    <p class="body-text">Lorem ipsum dolor sit amet, consectetur adipiscing elit, sed do eiusmod tempor incididunt ut labore et dolore magna aliqua. Quis ipsum suspendisse ultrices gravida. Risus commodo viverra maecenas accumsan lacus vel facilisis. Lorem Ipsum is simply dummy text of the printing and typesetting industry. Lorem Ipsum has been the industry's standard dummy text.</p>
  </div>
  <div class="icon-row" style="top:440px">
    <span class="icon-badge"><svg width="22" height="22" viewBox="0 0 22 22"><path d="M4 19V6h14v13z M8 10h2 M12 10h2 M8 14h2 M12 14h2" fill="none" stroke="#2f9fe0" stroke-width="1.5"/></svg></span>
    <p class="body-text">Lorem ipsum dolor sit amet, consectetur adipiscing elit, sed do eiusmod tempor incididunt ut labore et dolore magna aliqua. Quis ipsum suspendisse ultrices gravida. Risus commodo viverra maecenas accumsan lacus vel facilisis. Lorem Ipsum is simply dummy text of the printing and typesetting industry. Lorem Ipsum has been the industry's standard dummy text.</p>
  </div>
  <div class="icon-row" style="top:508px">
    <span class="icon-badge"><svg width="22" height="22" viewBox="0 0 22 22"><path d="M4 19h14 M6 19V9h10v10 M8 9V5h6v4" fill="none" stroke="#2f9fe0" stroke-width="1.5"/></svg></span>
    <p class="body-text">Lorem ipsum dolor sit amet, consectetur adipiscing elit, sed do eiusmod tempor incididunt ut labore et dolore magna aliqua. Quis ipsum suspendisse ultrices gravida. Risus commodo viverra maecenas accumsan lacus vel facilisis. Lorem Ipsum is simply dummy text of the printing and typesetting industry. Lorem Ipsum has been the industry's standard dummy text.</p>
  </div>
  <div class="folio">03</div>
</section>

<!-- Section 1 continued -->
<section class="page p-four">
  <header class="running-head"><span class="doc-title">COMMERCIAL WASTEWATER</span><span class="site">www.vantrelo.com.au</span></header>
  <h2 class="h-sub" style="position:absolute;left:30px;top:96px">1.2 Heading Here</h2>
  <div class="two-col" style="top:130px">
    <p class="body-text">Lorem ipsum dolor sit amet, consectetur adipiscing elit, sed do eiusmod tempor incididunt ut labore et dolore magna aliqua. Quis ipsum suspendisse ultrices gravida. Risus commodo viverra maecenas accumsan lacus vel facilisis. Lorem Ipsum is simply dummy text of the printing and typesetting industry. Lorem Ipsum has been the industry's standard dummy text.</p>
    <p class="body-text">Lorem ipsum dolor sit amet, consectetur adipiscing elit, sed do eiusmod tempor incididunt ut labore et dolore magna aliqua. Quis ipsum suspendisse ultrices gravida. Risus commodo viverra maecenas accumsan lacus vel facilisis. Lorem Ipsum is simply dummy text of the printing and typesetting industry. Lorem Ipsum has been the industry's standard dummy text.</p>
  </div>
  <div class="photo" style="left:33px;top:249px;width:465px;height:203px;border-radius:16px;background:linear-gradient(180deg,#8fb07a 0%,#4f7a3a 40%,#e8ece8 60%,#6f9a52 100%)" role="img" aria-label="Outdoor event venue with rows of white chairs on a lawn"></div>
  <h2 class="h-sub" style="position:absolute;left:30px;top:478px">1.3 Heading Here</h2>
  <div class="two-col" style="top:512px">
    <div><div class="bullet-head">LOREM IPSUM DOLOR SIT AMET</div><p class="bullet-body">Lorem Ipsum is simply dummy text of the printing and typesetting industry. Lorem Ipsum has been the industry's standard dummy.</p></div>
    <div><div class="bullet-head">LOREM IPSUM DOLOR SIT AMET</div><p class="bullet-body">Lorem Ipsum is simply dummy text of the printing and typesetting industry. Lorem Ipsum has been the industry's standard dummy.</p></div>
  </div>
  <div class="folio">04</div>
</section>

<!-- Section 2 -->
<section class="page p-five">
  <header class="running-head"><span class="doc-title">COMMERCIAL WASTEWATER</span><span class="site">www.vantrelo.com.au</span></header>
  <div class="table-band"></div>
  <h1 class="h-section" style="position:absolute;left:30px;top:66px">2. Heading Here</h1>
  <p class="body-text" style="position:absolute;left:270px;top:66px;width:230px">Lorem ipsum dolor sit amet, consectetur adipiscing elit, sed do eiusmod tempor incididunt ut labore et dolore magna aliqua. Quis ipsum suspendisse ultrices gravida. Risus commodo viverra maecenas accumsan lacus vel facilisis. Lorem Ipsum is simply dummy text.</p>
  <table class="data-table">
    <tr><th>LOREM IPSUM</th><th>LOREM 1</th><th>LOREM 2</th><th>LOREM 3</th><th>LOREM 4</th><th>LOREM 5</th><th>LOREM 6</th></tr>
    <tr><td class="row-label">Title 1</td><td>✕</td><td>✓</td><td>✕</td><td>✓</td><td>✕</td><td>✓</td></tr>
    <tr><td class="row-label">Title 2</td><td>✓</td><td>✓</td><td>✕</td><td>✓</td><td>✓</td><td>✓</td></tr>
    <tr><td class="row-label">Title 3</td><td>✕</td><td>✓</td><td>✕</td><td>✓</td><td>✕</td><td>✓</td></tr>
    <tr><td class="row-label">Title 4</td><td>✓</td><td>✕</td><td>✓</td><td>✕</td><td>✓</td><td>✓</td></tr>
    <tr><td class="row-label">Title 5</td><td>✕</td><td>✓</td><td>✓</td><td>✓</td><td>✕</td><td>✓</td></tr>
  </table>
  <h2 class="h-sub" style="position:absolute;left:30px;top:340px">2.1 Heading Here</h2>
  <p class="body-text" style="position:absolute;left:30px;top:374px;width:470px">Lorem ipsum dolor sit amet, consectetur adipiscing elit, sed do eiusmod tempor incididunt ut labore et dolore magna aliqua. Quis ipsum suspendisse ultrices gravida. Risus commodo viverra maecenas accumsan lacus vel facilisis. Lorem Ipsum is simply dummy text of the printing and typesetting industry. Lorem Ipsum has been the industry's standard dummy text.</p>
  <div class="icon-row" style="top:440px">
    <span class="icon-badge"><svg width="22" height="22" viewBox="0 0 22 22"><path d="M3 19V9l8-6 8 6v10H3z M9 19v-6h4v6" fill="none" stroke="#2f9fe0" stroke-width="1.5"/></svg></span>
    <p class="body-text">Lorem ipsum dolor sit amet, consectetur adipiscing elit, sed do eiusmod tempor incididunt ut labore et dolore magna aliqua. Quis ipsum suspendisse ultrices gravida. Risus commodo viverra maecenas accumsan lacus vel facilisis. Lorem Ipsum is simply dummy text of the printing and typesetting industry. Lorem Ipsum has been the industry's standard dummy text.</p>
  </div>
  <div class="icon-row flip" style="top:520px">
    <span class="icon-badge"><svg width="22" height="22" viewBox="0 0 22 22"><path d="M4 19h14 M6 19V9h10v10 M8 9V5h6v4" fill="none" stroke="#2f9fe0" stroke-width="1.5"/></svg></span>
    <p class="body-text">Lorem ipsum dolor sit amet, consectetur adipiscing elit, sed do eiusmod tempor incididunt ut labore et dolore magna aliqua. Quis ipsum suspendisse ultrices gravida. Risus commodo viverra maecenas accumsan lacus vel facilisis. Lorem Ipsum is simply dummy text of the printing and typesetting industry. Lorem Ipsum has been the industry's standard dummy text.</p>
  </div>
  <div class="folio">05</div>
</section>

<!-- Section 2 continued -->
<section class="page p-six">
  <header class="running-head"><span class="doc-title">COMMERCIAL WASTEWATER</span><span class="site">www.vantrelo.com.au</span></header>
  <div class="icon-row" style="top:50px">
    <span class="icon-badge"><svg width="22" height="22" viewBox="0 0 22 22"><path d="M3 19V9l8-6 8 6v10H3z M9 19v-6h4v6" fill="none" stroke="#2f9fe0" stroke-width="1.5"/></svg></span>
    <p class="body-text">Lorem ipsum dolor sit amet, consectetur adipiscing elit, sed do eiusmod tempor incididunt ut labore et dolore magna aliqua. Quis ipsum suspendisse ultrices gravida. Risus commodo viverra maecenas accumsan lacus vel facilisis. Lorem Ipsum is simply dummy text of the printing and typesetting industry. Lorem Ipsum has been the industry's standard dummy text.</p>
  </div>
  <div class="icon-row flip" style="top:130px">
    <span class="icon-badge"><svg width="22" height="22" viewBox="0 0 22 22"><path d="M4 19V6h14v13z M8 10h2 M12 10h2 M8 14h2 M12 14h2" fill="none" stroke="#2f9fe0" stroke-width="1.5"/></svg></span>
    <p class="body-text">Lorem ipsum dolor sit amet, consectetur adipiscing elit, sed do eiusmod tempor incididunt ut labore et dolore magna aliqua. Quis ipsum suspendisse ultrices gravida. Risus commodo viverra maecenas accumsan lacus vel facilisis. Lorem Ipsum is simply dummy text of the printing and typesetting industry. Lorem Ipsum has been the industry's standard dummy text.</p>
  </div>
  <div class="icon-row" style="top:210px">
    <span class="icon-badge"><svg width="22" height="22" viewBox="0 0 22 22"><path d="M3 19V9l8-6 8 6v10H3z M9 19v-6h4v6" fill="none" stroke="#2f9fe0" stroke-width="1.5"/></svg></span>
    <p class="body-text">Lorem ipsum dolor sit amet, consectetur adipiscing elit, sed do eiusmod tempor incididunt ut labore et dolore magna aliqua. Quis ipsum suspendisse ultrices gravida. Risus commodo viverra maecenas accumsan lacus vel facilisis. Lorem Ipsum is simply dummy text of the printing and typesetting industry. Lorem Ipsum has been the industry's standard dummy text.</p>
  </div>
  <div class="icon-row flip" style="top:290px">
    <span class="icon-badge"><svg width="22" height="22" viewBox="0 0 22 22"><path d="M4 19h14 M6 19V9h10v10 M8 9V5h6v4" fill="none" stroke="#2f9fe0" stroke-width="1.5"/></svg></span>
    <p class="body-text">Lorem ipsum dolor sit amet, consectetur adipiscing elit, sed do eiusmod tempor incididunt ut labore et dolore magna aliqua. Quis ipsum suspendisse ultrices gravida. Risus commodo viverra maecenas accumsan lacus vel facilisis. Lorem Ipsum is simply dummy text of the printing and typesetting industry. Lorem Ipsum has been the industry's standard dummy text.</p>
  </div>
  <div class="photo" style="left:33px;top:425px;width:465px;height:163px;border-radius:16px;background:linear-gradient(160deg,#6d8c5a 0%,#8aa36f 45%,#9bb8c9 75%,#5d86a6 100%)" role="img" aria-label="Aerial view of a resort beside a lake"></div>
  <div class="folio">06</div>
</section>

</body>
</html>
```